Innovative psychologist for companies seeks web design for website

Psychologist offers 2 topics:
1. What can a company do to ensure that employees are satisfied and enjoy their work?
The following explanatory video is linked on the website:
https://www.clipvarno.com/watch?v=qTrmWbLpoZd
2. How can you successfully change your own behavior?
Explanatory video: https://www.clipvarno.com/watch?v=HwkPZaGuoTb&t=6s
The slogan for the second theme will be: YOU are the pirate of your life!

Target Market(s)

companies and private individuals

Number of Pages Required

1 page

Requirements
Nice to have
• Characteristics of the psychologist: pragmatic, down-to-earth, honest, direct, appreciative, enjoys life, loves nature

```html
<!DOCTYPE html>
<html lang="en">
<head>
<meta charset="utf-8">
<title>Lukas Brenner – Psychologist</title>
<link href="https://fonts.googleapis.com/css2?family=Montserrat:wght@400;500;600;700&family=Josefin+Sans:wght@400;600&display=swap" rel="stylesheet">
<style>
:root{
  --red:#e8401c;
  --red-dark:#d8361a;
  --blue:#1a94d6;
  --blue-dark:#0e7fc0;
  --ink:#1f1f1f;
  --text:#4a4a4a;
  --pale:#eef4f8;
  --white:#fff;
  --line:#c9d3da;
}
*{margin:0;padding:0;box-sizing:border-box}
html,body{width:1200px;height:4082px;overflow:hidden;background:var(--white)}
body{position:relative;font-family:"Montserrat",sans-serif;color:var(--ink)}
a{color:inherit;text-decoration:none}
.abs{position:absolute}
.display{font-family:"Josefin Sans",sans-serif}
.hl-blue{background:var(--blue);color:var(--white);padding:2px 8px;border-radius:4px}
.hl-red{background:var(--red);color:var(--white);padding:2px 8px;border-radius:4px}
.dash{display:block;width:52px;height:3px;background:linear-gradient(90deg,var(--red) 0 65%,transparent 65% 78%,var(--red) 78%)}
.btn{display:inline-flex;align-items:center;justify-content:center;border-radius:30px;color:var(--white);font-weight:700;letter-spacing:.5px}

/* header */
.site-header{left:0;top:0;width:1200px;height:84px;z-index:3}
.brand{left:95px;top:18px;display:flex;align-items:center;gap:12px;font-family:"Josefin Sans",sans-serif;font-size:25px;color:var(--red);font-weight:600}
.brand-dot{width:42px;height:42px;border-radius:50%;background:var(--blue)}
.nav{left:440px;top:33px;display:flex;gap:26px;font-size:13px;font-weight:600}
.nav a:nth-child(4){margin-left:4px}
.phone-btn{left:962px;top:24px;width:173px;height:36px;background:var(--red);font-size:13px;font-weight:500;gap:6px}

/* hero */
.hero{left:0;top:0;width:1200px;height:702px;border-bottom-left-radius:180px;overflow:hidden;
  background:linear-gradient(100deg,#d7e5ef 0%,#c3d8e7 40%,#a9c4d6 62%,#b8b2a0 88%,#c9b99b 100%)}
.hero-photo{right:0;top:0;width:560px;height:702px;background:linear-gradient(180deg,rgba(140,140,140,.35),rgba(110,110,110,.55))}
.hero-tag{left:106px;top:237px;background:var(--red);color:var(--white);font-size:29px;padding:6px 14px 3px;font-family:"Josefin Sans",sans-serif}
.hero-title{left:110px;top:290px;font-family:"Josefin Sans",sans-serif;font-size:50px;line-height:60px;font-weight:600;color:#1d2a38}
.hero-btn{left:114px;top:425px;width:197px;height:50px;background:var(--blue);font-size:15px}

/* about */
.about-ring{left:87px;top:749px;width:492px;height:492px;border-radius:50%;border:2px solid #9fd1ee}
.about-photo{left:100px;top:762px;width:466px;height:466px;border-radius:50%;background:linear-gradient(160deg,#8d8a86,#3d5b86 60%,#2c4470);border:8px solid var(--blue)}
.about-title{left:614px;top:820px;font-size:42px;color:var(--red);font-family:"Josefin Sans",sans-serif}
.about-title .hl-blue{font-size:42px}
.about-dash{left:616px;top:883px}
.about-text{left:616px;top:908px;width:470px;font-size:16px;line-height:25px;color:var(--text)}
.about-text p+p{margin-top:24px}
.about-btn{left:613px;top:1117px;width:180px;height:48px;background:var(--red);font-size:14px}

/* company */
.company{left:0;top:1271px;width:1200px;height:587px;background:var(--pale);border-top-right-radius:180px}
.company-card{left:63px;top:1328px;width:655px;height:466px;background:var(--white);border-top-left-radius:120px;box-shadow:0 6px 24px rgba(0,0,0,.05)}
.company-title{left:130px;top:1410px;width:500px;font-size:31px;line-height:42px;font-family:"Josefin Sans",sans-serif}
.company-dash{left:132px;top:1551px}
.company-text{left:131px;top:1577px;width:460px;font-size:15px;line-height:24px;color:var(--text)}
.frame-blue{left:840px;top:1397px;width:288px;height:357px;background:var(--blue)}
.video{display:block}
.video-1{left:632px;top:1411px;width:487px;height:333px;background:linear-gradient(180deg,#9ea4aa,#d5dde3 45%,#5c8fb2);border:3px solid #555}
.play{position:absolute;left:50%;top:50%;transform:translate(-50%,-50%)}

/* behavior */
.behavior{left:0;top:1858px;width:1200px;height:618px;background:linear-gradient(180deg,#1597dc,#0f86ca);border-bottom-left-radius:170px}
.behavior-title{left:0;top:1924px;width:1200px;text-align:center;font-size:41px;line-height:52px;color:var(--white);font-family:"Josefin Sans",sans-serif}
.behavior-dash{left:574px;top:2033px;background:linear-gradient(90deg,var(--white) 0 65%,transparent 65% 78%,var(--white) 78%)}
.behavior-text{left:200px;top:2056px;width:800px;text-align:center;color:var(--white);font-size:17px;line-height:25px}
.frame-white{left:256px;top:2154px;width:186px;height:220px;background:var(--white)}
.frame-red{left:740px;top:2380px;width:190px;height:187px;background:var(--red)}
.video-2{left:266px;top:2165px;width:655px;height:392px;background:linear-gradient(180deg,#b9d6e6,#a9a07f 45%,#6b7a52 80%,#a78e6c)}

/* blogs */
.blogs-title{left:115px;top:2622px;font-size:41px;color:var(--red);font-family:"Josefin Sans",sans-serif}
.blogs-dash{left:117px;top:2683px}
.blog-main{left:114px;top:2717px;width:506px;height:401px;background:linear-gradient(170deg,#f2b54c,#e2863a 50%,#8a5a3e)}
.blog-main .meta{position:absolute;left:35px;bottom:20px;color:var(--white)}
.date{display:inline-flex;align-items:center;gap:5px;background:var(--blue);color:var(--white);font-size:11px;font-weight:700;padding:3px 8px}
.date i{width:10px;height:10px;border:2px solid var(--white);border-radius:50%}
.blog-main h3{font-size:17px;font-weight:700;margin:10px 0 6px 0}
.blog-main p{font-size:14px;line-height:17px}
.blog-card{left:632px;width:465px;height:190px;border:1px solid var(--line);background:var(--white);display:flex}
.blog-card .thumb{width:223px;height:100%}
.blog-card .body{padding:26px 0 0 26px;width:240px}
.blog-card .date{font-size:10px;padding:2px 6px}
.blog-card h4{font-size:14px;font-weight:700;margin:12px 0 6px}
.blog-card p{font-size:11px;line-height:16px;color:var(--text)}
.blog-card .more{display:inline-block;margin-top:10px;border:1px solid var(--red);color:var(--red);font-size:9px;font-weight:600;padding:5px 18px}

/* contact */
.contact{left:120px;top:3233px;width:967px;height:527px;border-top-left-radius:120px;border-bottom-right-radius:120px;
  background:linear-gradient(120deg,#f04a1c,#e33c16 55%,#ee6a2f)}
.contact-title{left:120px;top:3280px;width:967px;text-align:center;font-size:44px;color:var(--white);font-family:"Josefin Sans",sans-serif}
.contact-title .hl-blue{font-size:44px}
.contact-dash{left:574px;top:3336px;background:linear-gradient(90deg,var(--white) 0 65%,transparent 65% 78%,var(--white) 78%)}
.contact-sub{left:120px;top:3356px;width:967px;text-align:center;font-size:18px;color:var(--white)}
.field{background:var(--white);font-size:12px;color:#444;padding:16px 19px}
.send{left:526px;top:3655px;width:181px;height:41px;background:var(--blue);color:var(--white);font-size:13px;font-weight:700;display:flex;align-items:center;justify-content:center}

/* footer */
.foot-brand-dot{left:580px;top:3783px;width:40px;height:40px;border-radius:50%;background:var(--blue)}
.foot-rule{left:118px;width:995px;height:1px;background:var(--line)}
.foot-name{left:456px;top:3856px;font-size:29px;color:var(--red);font-family:"Josefin Sans",sans-serif;font-weight:600}
.foot-contact{top:3858px;display:flex;align-items:center;gap:12px;font-size:16px}
.foot-contact .ic{width:34px;height:34px;border-radius:50%;background:var(--red);display:flex;align-items:center;justify-content:center}
.foot-nav{left:300px;top:3934px;display:flex;gap:32px;font-size:14px;font-weight:600}
.foot-nav span{color:var(--blue)}
.copy{left:0;top:3982px;width:1200px;text-align:center;font-size:13px;color:var(--text)}
.socials{left:518px;top:4017px;display:flex;gap:14px}
.socials a{width:36px;height:36px;border-radius:50%;background:var(--blue)}
</style>
</head>
<body>

<div class="abs hero">
  <div class="abs hero-photo" role="img" aria-label="Photo of a smiling man stretching joyfully outdoors above a cliff"></div>
</div>

<header class="abs site-header">
  <a class="abs brand" href="#"><span class="brand-dot"></span>LUKAS BRENNER</a>
  <nav class="abs nav">
    <a href="#about">ABOUT</a>
    <a href="#behavior">CHANGE BEHAVIOR</a>
    <a href="#company">EMPLOYEE SATISFIED</a>
    <a href="#contact">CONTACT</a>
  </nav>
  <a class="abs btn phone-btn" href="#">
    <svg width="14" height="14" viewBox="0 0 24 24" fill="none" stroke="#fff" stroke-width="2.2"><path d="M5 3h4l2 5-3 2a11 11 0 0 0 6 6l2-3 5 2v4a2 2 0 0 1-2 2A18 18 0 0 1 3 5a2 2 0 0 1 2-2z"/></svg>
    (+123) 555 0142
  </a>
</header>

<div class="abs hero-tag">LUKAS BRENNER</div>
<h1 class="abs hero-title">YOU ARE THE PIRATE<br>OF YOUR LIFE!</h1>
<a class="abs btn hero-btn" href="#contact">CONTACT ME</a>

<section id="about">
  <div class="abs about-ring"></div>
  <div class="abs about-photo" role="img" aria-label="Portrait photo of the psychologist in a denim shirt and glasses"></div>
  <h2 class="abs about-title">About Lukas <span class="hl-blue">Brenner</span></h2>
  <span class="abs dash about-dash"></span>
  <div class="abs about-text">
    <p>Lorem ipsum dolor sit amet, consectetur adipiscing elit, sed do eiusmod tempor incididunt ut labore et dolore</p>
    <p>Aagna aliqua Ut enim ad minim veniam, quis nostrud exercitation ullamco laboris nisi ut aliquip ex ea commodo consequat. Duis aute irure dolor in reprehenderit in voluptate velit esse cillum dolore eu fu</p>
  </div>
  <a class="abs btn about-btn" href="#">LEARN MORE</a>
</section>

<section id="company">
  <div class="abs company"></div>
  <div class="abs company-card"></div>
  <h2 class="abs company-title">What can a company do to ensure that employees are satisfied and <span class="hl-red">enjoy their work?</span></h2>
  <span class="abs dash company-dash"></span>
  <p class="abs company-text">Lorem ipsum dolor sit amet, consectetur adipiscing elit, sed do eiusmod tempor incididunt ut labore et dolore magna aliqua. Ut enim ad minim veniam, quis nostrud exercitation ullamco laboris nisi ut aliquip ex ea</p>
  <div class="abs frame-blue"></div>
  <a class="abs video video-1" href="https://www.clipvarno.com/watch?v=qTrmWbLpoZd" role="img" aria-label="Cartoon illustration of two men shaking hands in an office, explanatory video">
    <svg class="play" width="64" height="64" viewBox="0 0 64 64"><circle cx="32" cy="32" r="28" fill="#fff" stroke="#111" stroke-width="4"/><path d="M25 19l20 13-20 13z" fill="#111"/></svg>
  </a>
</section>

<section id="behavior">
  <div class="abs behavior"></div>
  <h2 class="abs behavior-title">How can you <span class="hl-red">Successfully change</span><br>your own behavior?</h2>
  <span class="abs dash behavior-dash"></span>
  <p class="abs behavior-text">Lorem ipsum dolor sit amet, consectetur adipiscing elit, sed do eiusmod tempor incididunt ut labore et dolore magna aliqua. Ut enim ad minim veniam</p>
  <div class="abs frame-white"></div>
  <div class="abs frame-red"></div>
  <a class="abs video video-2" href="https://www.clipvarno.com/watch?v=HwkPZaGuoTb&amp;t=6s" role="img" aria-label="Cartoon illustration of a thoughtful man before an open garden gate, explanatory video">
    <svg class="play" width="72" height="72" viewBox="0 0 72 72"><circle cx="36" cy="36" r="32" fill="none" stroke="#fff" stroke-width="5"/><path d="M29 22l20 14-20 14z" fill="#fff"/></svg>
  </a>
</section>

<section id="blogs">
  <h2 class="abs blogs-title">Latest <span class="hl-blue">Blogs</span></h2>
  <span class="abs dash blogs-dash"></span>
  <article class="abs blog-main" role="img" aria-label="Photo of a happy woman raising her arms at sunset">
    <div class="meta">
      <span class="date"><i></i>11 FEB 2024</span>
      <h3>Sed ut perspiciatis unde</h3>
      <p>Lorem ipsum dolor sit amet, consectetur adipiscing elit,<br>sed do eiusmod tempor incididunt</p>
    </div>
  </article>
  <article class="abs blog-card" style="top:2717px">
    <div class="thumb" role="img" aria-label="Photo of a therapist taking notes during a session" style="background:linear-gradient(135deg,#d9dcd8,#8f9aa3)"></div>
    <div class="body">
      <span class="date"><i></i>19 JAN 2024</span>
      <h4>Neque porro quisquam</h4>
      <p>Lorem ipsum dolor sit amet, consectetur adipiscing elit, sed do eiusmod tempor incididunt</p>
      <a class="more" href="#">LEARN MORE</a>
    </div>
  </article>
  <article class="abs blog-card" style="top:2923px">
    <div class="thumb" role="img" aria-label="Photo of a woman with open arms in a field at dawn" style="background:linear-gradient(180deg,#e9d3a8,#c79a5e 60%,#6e5a3d)"></div>
    <div class="body">
      <span class="date"><i></i>19 JAN 2024</span>
      <h4>Neque porro quisquam</h4>
      <p>Lorem ipsum dolor sit amet, consectetur adipiscing elit, sed do eiusmod tempor incididunt</p>
      <a class="more" href="#">LEARN MORE</a>
    </div>
  </article>
</section>

<section id="contact">
  <div class="abs contact"></div>
  <h2 class="abs contact-title">Get in touch <span class="hl-blue">with me</span></h2>
  <span class="abs dash contact-dash"></span>
  <p class="abs contact-sub">Leave us a message &amp; I will contact you shortly.</p>
  <div class="abs field" style="left:287px;top:3412px;width:307px;height:48px">First Name</div>
  <div class="abs field" style="left:602px;top:3412px;width:309px;height:48px">Last Name</div>
  <div class="abs field" style="left:287px;top:3474px;width:307px;height:48px">Email address</div>
  <div class="abs field" style="left:602px;top:3474px;width:309px;height:48px">Phone number</div>
  <div class="abs field" style="left:287px;top:3536px;width:624px;height:100px;padding-top:14px">Message</div>
  <a class="abs send" href="#">SEND MESSAGE</a>
</section>

<footer>
  <div class="abs foot-brand-dot"></div>
  <div class="abs foot-rule" style="top:3837px"></div>
  <div class="abs foot-contact" style="left:150px">
    <span class="ic"><svg width="16" height="16" viewBox="0 0 24 24" fill="#fff"><path d="M5 3h4l2 5-3 2a11 11 0 0 0 6 6l2-3 5 2v4a2 2 0 0 1-2 2A18 18 0 0 1 3 5a2 2 0 0 1 2-2z"/></svg></span>
    (+123) 555 01420
  </div>
  <div class="abs foot-name">LUKAS BRENNER</div>
  <div class="abs foot-contact" style="left:816px">
    <span class="ic"><svg width="18" height="14" viewBox="0 0 24 18" fill="none" stroke="#fff" stroke-width="2"><rect x="1" y="1" width="22" height="16" rx="2"/><path d="M1 2l11 8 11-8"/></svg></span>
    info@lukasbrenner.com
  </div>
  <div class="abs foot-rule" style="top:3909px"></div>
  <nav class="abs foot-nav">
    <a href="#">HOME</a><span>|</span>
    <a href="#about">ABOUT US</a><span>|</span>
    <a href="#">SERVICES</a><span>|</span>
    <a href="#">VIDEOS</a><span>|</span>
    <a href="#contact">CONTACT US</a>
  </nav>
  <p class="abs copy">Copyright 2024 Lukas Brenner. All Right Reserved</p>
  <div class="abs socials">
    <a href="#" aria-label="Social profile 1"></a>
    <a href="#" aria-label="Social profile 2"></a>
    <a href="#" aria-label="Social profile 3"></a>
  </div>
</footer>

</body>
</html>
```